Completely Coded Dog Community Website - Mobile Centric & Highly Responsive

We need a completely coded design based in Wordpress CMS that is designed with mobile in mind first! I would like to carry over the style of our current website (brightkennel.c0m) into the design of the responsive website. In addition, please only submit designs if you provide high quality admin support, as the winning design will likely be hired to provide monthly support forward at $100/month (SEO skill set valued). Also am looking for a quote on an iphone and android app so please submit designs only if you have capability to create the highest quality apps. No cheap looking template submissions please...will need form, chat, sign in and e-commerce integration. I have vector files if needed for website.
Updates

Project Deadline Extended
Reason: Want to see more mobile friendly, modern designs and responses to willingness for web admin support going forward. Thanks

Target Market(s)

Adults based in the USA aged 25-50 that own dogs

Industry/Entity Type

E-Commerce

Requirements
Must have
• Pages:
Home Page
About Us
Contact Us
Dog Deals
Videos
Photos
Health
Training
Breeds
Ask the Dog Expert
Dog Product Reviews
Dog Stories
Dog Friendly Travel
Dog Care
Contests
Nice to have
• SEO
Metatags
Unique page layouts
Social integration to our social media accounts
Social API logins
Should not have
• Cheap template look
Not consistent with previous color scheme
Different logo than our current options

```html
<!DOCTYPE html>
<html lang="en">
<head>
<meta charset="utf-8">
<title>Bright Kennel – Home</title>
<link href="https://fonts.googleapis.com/css2?family=Comic+Neue:wght@400;700&display=swap" rel="stylesheet">
<style>
:root{
  --teal:#3a8699;
  --teal-dark:#2f7486;
  --teal-text:#2f7a8c;
  --footer:#52a9c4;
  --footer-dark:#3b8ca5;
  --orange:#f9a93b;
  --panel-top:#dcedf8;
  --panel:#eaf5fc;
  --white:#ffffff;
  --line:#9fb3bd;
}
*{box-sizing:border-box;margin:0;padding:0}
html,body{width:1200px;height:1000px;overflow:hidden;background:var(--white);font-family:"Comic Neue",cursive}
.page{position:relative;width:1200px;height:1000px}
.side-photo{position:absolute;left:201px;top:0;width:117px;height:1000px;
  background:linear-gradient(180deg,#8c8f92 0%,#c9873a 18%,#f5b23a 30%,#e59a35 38%,#3d4a58 45%,#6b5f55 60%,#3a3430 80%,#2a2725 100%)}
.main{position:absolute;left:318px;top:0;width:593px;height:1000px;
  background:linear-gradient(180deg,var(--panel-top) 0%,#f1f8fd 22%,var(--panel) 60%,var(--panel) 100%)}
.tab-icon{position:absolute;left:269px;top:39px;width:48px;height:48px;background:var(--teal-dark);display:flex;align-items:center;justify-content:center}
.tab{position:absolute;left:318px;top:39px;width:217px;height:48px;background:#3d8498;color:var(--white);font-size:16px;font-weight:700;line-height:48px;text-align:right;padding-right:32px}
.brand{position:absolute;left:782px;top:62px;display:flex;align-items:center;gap:6px;color:var(--teal-text);font-weight:700;font-size:16px}
.brand i{width:12px;height:12px;border-radius:50%;background:var(--orange);display:block}
.welcome{position:absolute;left:375px;top:142px;color:var(--teal-text);font-size:26px;line-height:30px}
.welcome span{color:var(--orange)}
.search{position:absolute;left:688px;top:161px;width:166px;height:27px;border:1px solid var(--teal-dark);background:#eef7fc;display:flex}
.search input{flex:1;border:0;background:transparent;font:11px "Comic Neue",cursive;padding-left:6px;color:#7a8a92}
.search button{width:28px;border:0;background:var(--footer-dark);display:flex;align-items:center;justify-content:center}
.divider{position:absolute;left:318px;top:260px;width:593px;height:1px;background:var(--line)}
.card{position:absolute;width:144px;text-align:center}
.card .photo{position:relative;height:136px;overflow:hidden}
.card .check{position:absolute;left:0;top:30px;width:28px;height:20px;background:#4ea5c0;display:flex;align-items:center;justify-content:center}
.card .ribbon{position:absolute;right:-18px;top:6px;width:70px;height:16px;background:var(--orange);color:var(--white);font-size:11px;font-weight:700;line-height:16px;transform:rotate(45deg)}
.card .label{margin-top:5px;height:24px;line-height:24px;background:var(--orange);color:var(--white);font-size:15px;font-weight:700}
.card .sub{margin-top:3px;font-size:11px;color:var(--teal-text)}
.card .vote{font-size:15px;color:var(--teal-text);line-height:18px}
.footer{position:absolute;left:318px;top:797px;width:593px;height:178px;background:var(--footer);color:var(--white)}
.col{position:absolute;top:25px}
.col h3{font-size:18px;font-weight:700;margin-bottom:6px}
.col li{list-style:none;font-size:10px;font-weight:700;line-height:15px;border-bottom:1px solid #7cc0d4;width:164px;padding-left:2px;margin-bottom:1px;white-space:nowrap}
.col li::before{content:"› ";font-size:13px}
.subscribe{position:absolute;left:403px;top:53px;width:167px;height:96px;background:var(--footer-dark);padding:5px}
.subscribe .field{height:25px;background:#eaf5fa;margin-bottom:6px;font-size:9px;color:#8a9aa2;line-height:25px;padding-left:5px;display:flex;justify-content:space-between;padding-right:6px}
.subscribe .btn{height:24px;background:var(--orange);font-size:11px;font-weight:700;text-align:center;line-height:24px;color:var(--white)}
.copyright{position:absolute;left:318px;top:975px;width:593px;height:25px;background:var(--white);color:var(--teal-text);font-size:12px;font-weight:700;text-align:center;line-height:25px}
.nav{position:absolute;left:911px;top:0;width:88px;height:1000px;background:var(--teal)}
.nav a{position:absolute;left:11px;color:var(--white);font-size:10px;font-weight:700;text-decoration:none;letter-spacing:.2px;white-space:nowrap}
</style>
</head>
<body>
<div class="page">
  <div class="side-photo" role="img" aria-label="Photo of a dog silhouetted against a sunset over the sea"></div>
  <div class="main"></div>

  <div class="tab-icon"><svg width="22" height="20" viewBox="0 0 22 20"><rect x="1" y="3" width="16" height="14" fill="none" stroke="#fff" stroke-width="1.5"/><rect x="5" y="1" width="16" height="14" fill="#2f7486" stroke="#fff" stroke-width="1.5"/><path d="M7 13l4-5 3 3 2-2 3 4z" fill="#fff"/></svg></div>
  <div class="tab">Home</div>

  <div class="brand"><i></i>BrightKennel</div>

  <h1 class="welcome" style="font-weight:400">Welcome<br>to <span>Bright Kennel</span></h1>

  <div class="search"><input type="text" placeholder="Search"><button aria-label="Search"><svg width="13" height="13" viewBox="0 0 13 13"><circle cx="5" cy="5" r="4" fill="none" stroke="#fff" stroke-width="1.6"/><path d="M8 8l4 4" stroke="#fff" stroke-width="1.8"/></svg></button></div>

  <div class="divider"></div>

  <div class="card" style="left:375px;top:319px"><div class="photo" role="img" aria-label="Golden retriever puppy photo" style="background:linear-gradient(135deg,#f3f1ee,#d9b27a)"><span class="check"><svg width="14" height="11" viewBox="0 0 14 11"><path d="M1 6l4 4 8-9" fill="none" stroke="#fff" stroke-width="2.2"/></svg></span></div><div class="label">Who is Cute</div><div class="sub">Must explain to you</div><div class="vote">Vote Now</div></div>

  <div class="card" style="left:543px;top:319px"><div class="photo" role="img" aria-label="White puppy on grass photo" style="background:linear-gradient(180deg,#7fb83c,#5a9a2a)"><span class="check"><svg width="14" height="11" viewBox="0 0 14 11"><path d="M1 6l4 4 8-9" fill="none" stroke="#fff" stroke-width="2.2"/></svg></span><span class="ribbon">new</span></div><div class="label">Who is Cute</div><div class="sub">Must explain to you</div><div class="vote">Vote Now</div></div>

  <div class="card" style="left:710px;top:319px"><div class="photo" role="img" aria-label="Labrador puppy photo" style="background:linear-gradient(135deg,#6fae3a,#efe4d0)"><span class="check"><svg width="14" height="11" viewBox="0 0 14 11"><path d="M1 6l4 4 8-9" fill="none" stroke="#fff" stroke-width="2.2"/></svg></span></div><div class="label">Who is Cute</div><div class="sub">Must explain to you</div><div class="vote">Vote Now</div></div>

  <div class="card" style="left:375px;top:542px"><div class="photo" role="img" aria-label="Beagle puppy photo" style="background:linear-gradient(135deg,#c2463a,#6a86a8 60%,#dfe6ea)"><span class="check"><svg width="14" height="11" viewBox="0 0 14 11"><path d="M1 6l4 4 8-9" fill="none" stroke="#fff" stroke-width="2.2"/></svg></span></div><div class="label">Who is Cute</div><div class="sub">Must explain to you</div><div class="vote">Vote Now</div></div>

  <div class="card" style="left:543px;top:542px"><div class="photo" role="img" aria-label="Tricolour puppy running on grass photo" style="background:linear-gradient(180deg,#6faa3a,#3d3430 60%,#5f9a2e)"><span class="check"><svg width="14" height="11" viewBox="0 0 14 11"><path d="M1 6l4 4 8-9" fill="none" stroke="#fff" stroke-width="2.2"/></svg></span><span class="ribbon">new</span></div><div class="label">Who is Cute</div><div class="sub">Must explain to you</div><div class="vote">Vote Now</div></div>

  <div class="card" style="left:710px;top:542px"><div class="photo" role="img" aria-label="White puppy on grass photo" style="background:linear-gradient(180deg,#86bb42,#f1ece0 60%,#5f9a2e)"><span class="check"><svg width="14" height="11" viewBox="0 0 14 11"><path d="M1 6l4 4 8-9" fill="none" stroke="#fff" stroke-width="2.2"/></svg></span><span class="ribbon">new</span></div><div class="label">Who is Cute</div><div class="sub">Must explain to you</div><div class="vote">Vote Now</div></div>

  <footer class="footer">
    <div class="col" style="left:22px"><h3>Most Popular:</h3><ul>
      <li>Demoralized by the charms consequat</li><li>Praising pain was born aspernatur</li><li>Exercitation ullamco laboris</li><li>Demoralized by the charms laboris</li><li>Praising pain was born vel eum</li><li>Exercitation ullamco laboris vel eum</li></ul></div>
    <div class="col" style="left:212px"><h3>Most Popular:</h3><ul>
      <li>Praising pain was born aspernatur</li><li>Demoralized by the charms laboris</li><li>Praising pain was born vel eum</li><li>Exercitation ullamco laboris vel eum</li></ul></div>
    <div class="col" style="left:403px"><h3>Subscribe Now:</h3></div>
    <form class="subscribe">
      <div class="field">Name<svg width="10" height="11" viewBox="0 0 10 11"><circle cx="5" cy="3" r="2.6" fill="#8a9aa2"/><path d="M0 11c0-4 10-4 10 0z" fill="#8a9aa2"/></svg></div>
      <div class="field">Mail<svg width="11" height="10" viewBox="0 0 11 10"><path d="M0 5l11-5-3 10-3-4z" fill="#8a9aa2"/></svg></div>
      <div class="btn">Subscribe Newsletter</div>
    </form>
  </footer>
  <div class="copyright">Copyright © 2015. www.brightkennel.c0m</div>

  <nav class="nav">
    <a style="top:16px">HOME</a>
    <a style="top:44px">ABOUT US</a>
    <a style="top:71px">CONTACT US</a>
    <a style="top:99px">DOG DEALS</a>
    <a style="top:126px">DOG STORIES</a>
    <a style="top:154px">PHOTOS</a>
    <a style="top:181px">HEALTH</a>
    <a style="top:209px">TRAINING</a>
    <a style="top:891px">PAWBOOK</a>
    <a style="top:918px">CHIRPER</a>
    <a style="top:946px">SEARCHLY+</a>
    <a style="top:974px">LINKUP</a>
  </nav>
</div>
</body>
</html>
```